依頼概要
■依頼の目的/概要
弊社が販売予定している玄米コーヒー(ドリップ式)のラベルデザインをお願いします。弊社は、穂波の里農園といいまして、自然農法栽培でお米や野菜を作っている農家です。信条は「土がきれいになれば世界が平和になる」です。今回の商品は健康食品としての位置づけになります。

■依頼詳細
今回は弊社が販売する玄米コーヒー(ドリップ式)のラベルのデザインをお願いします。
すでに、インスタント式の玄米コーヒーを販売しており、今回の商品はそれに続くプレミアム玄米コーヒーとして、前回よりも一段格上の商品を考えております。インスタント式は粉状ですが、今回の商品は粗挽きで本当の粗挽きコーヒーとほとんど変わらない色と形状です。入れた玄米コーヒーの色も、何も言わなければ本当のコーヒーと見分けがつきません。味もドリップ式はとっても美味しく、一度飲むと病みつきになります。

プレミアム玄米コーヒー(ドリップ式)の特徴は以下のとおりです。

●本当のコーヒーのようにドリップ式で美味しい玄米コーヒーが入れられます。
●使用している玄米は、自然農法栽培で作った、無肥料、無農薬のこだわりのお米を100%使用しています。
●コーヒーといっても、玄米飲料なのでノンカフェインで身体に優しいです。
●ポリフェノールや食物繊維が豊富に含まれていて、健康志向の人にはぴったりの飲料です。
●玄米には解毒作用があるようで、お通じが良くなり、身体の中をスッキリきれいにしてくれます。
(ちなみに初めて飲む方のなかには、下痢をされる方が多くいらっしゃいます。わたしもその一人でした。)
●内容量は200gです。

■その他の要望
●前回のインスタント式の商品の写真を添付してあります。前回は白のパッケージ(半透明、和紙風)でしたが、今回は濃い茶色(つや消し)のパッケージ(添付写真参照)になっており、高級感の漂うデザインが希望です。ドリップでコーヒーを入れている美しい写真をデザインにいれていただけると嬉しいです。(一目でドリップ式と分かる)
もちろん写真以外のデザインでも結構です。
●デザインの中に、穂波の里農園のロゴマークを入れてください。ファイルを添付してあります。
●パッケージの大きさは横140㎜×縦220㎜(190㎜)のチャック付スタンド袋です。

注意:表示法の関係で「自然農法」「無肥料」「無農薬」の言葉は使えません。
「自然栽培」「自然栽培法」「肥料不使用」「化学肥料不使用」「農薬不使用」の表記ならOKです。

その他何かご不明な点がございましたら、お気軽にご質問下さい。
デザイナーの皆様、どうぞよろしくお願いいたします!!
「ドリップ式」または「ドリップ用」という言葉をデザインの中に入れてください。
「プレミアム」という言葉も英語またはカタカナで入れてください。
■ 選んだ理由

私の希望通り、ドリップのシズル感と全体的な高級感がよく表現されていました。色の使い方が大変気に入りました。素晴らしいデザインを本当にありがとうございました。
とても満足しています。
また機会がありましたら、どうぞよろしくお願いいたします。

■ 提案者全員のお礼・コメント

この度は、たくさんの提案を頂きありがとうございました。
どれもすばらしいデザインばかりでした。
機会がありましたらまたよろしくお願いいたします。

```html
<!DOCTYPE html>
<html lang="ja">
<head>
<meta charset="UTF-8">
<title>プレミアム玄米珈琲 ドリップ式 ラベル</title>
<link href="https://fonts.googleapis.com/css2?family=Cormorant+Garamond:wght@500;600&family=Noto+Sans+JP:wght@700&family=Noto+Serif+JP:wght@500;700;900&display=swap" rel="stylesheet">
<style>
  :root {
    --page: #f4f1ec;
    --pouch-brown: #5a4139;
    --label-brown: #3b2019;
    --band-red: #8e1010;
    --band-red-dark: #5a0808;
    --gold: #e9c874;
    --white: #fbf7f0;
    --badge-green: #c8dc32;
    --badge-text: #3a2a10;
    --tag-red: #9a1515;
    --photo-top: #3b2019;
    --photo-mid: #7a5a40;
    --photo-low: #c7ab86;
  }
  * { margin: 0; padding: 0; box-sizing: border-box; }
  html, body { width: 692px; height: 1200px; overflow: hidden; }
  body { background: var(--page); position: relative; font-family: "Noto Serif JP", serif; color: var(--white); }

  .pouch {
    position: absolute; left: 28px; top: 24px; width: 636px; height: 1156px;
    background: var(--pouch-brown); border-radius: 10px;
  }

  .label {
    position: absolute; left: 50px; top: 150px; width: 600px; height: 770px;
    background: var(--label-brown);
    overflow: hidden;
  }

  .maker {
    position: absolute; top: 58px; left: 0; width: 100%;
    display: flex; align-items: center; justify-content: center; gap: 12px;
  }
  .maker-mark { width: 22px; height: 22px; border-radius: 50%; background: var(--white); }
  .maker-name {
    font-family: "Cormorant Garamond", serif; font-weight: 500;
    font-size: 34px; letter-spacing: 3px; color: var(--white);
  }

  .premium-band {
    position: absolute; top: 104px; left: 0; width: 100%; height: 32px;
    background: linear-gradient(180deg, var(--band-red) 0%, var(--band-red-dark) 100%);
    display: flex; align-items: center; justify-content: center;
  }
  .premium-word {
    font-family: "Cormorant Garamond", serif; font-weight: 600; font-size: 24px;
    letter-spacing: 20px; color: var(--gold); padding-left: 20px;
  }

  .product-name {
    position: absolute; top: 140px; left: 0; width: 100%; text-align: center;
    font-weight: 900; font-size: 94px; letter-spacing: 4px; line-height: 1.15;
  }

  .claim {
    position: absolute; top: 258px; left: 0; width: 100%; text-align: center;
    font-weight: 700; font-size: 27px; line-height: 1.4; letter-spacing: 3px;
  }

  .badges {
    position: absolute; top: 338px; left: 0; width: 100%;
    display: flex; flex-direction: column; align-items: center; gap: 12px;
  }
  .badge-row { display: flex; gap: 14px; }
  .badge {
    background: var(--badge-green); color: var(--badge-text);
    font-family: "Noto Serif JP", serif; font-weight: 700; font-size: 19px;
    padding: 2px 12px; border-radius: 6px; letter-spacing: 1px;
  }

  .drip-photo {
    position: absolute; left: 0; top: 420px; width: 100%; height: 350px;
    background: linear-gradient(180deg, var(--photo-top) 0%, var(--photo-mid) 45%, var(--photo-low) 100%);
  }

  .method-tag {
    position: absolute; left: 20px; top: 454px;
    background: var(--tag-red); border: 2px solid var(--white);
    font-weight: 700; font-size: 24px; letter-spacing: 1px;
    padding: 4px 12px;
  }

  .net-weight {
    position: absolute; right: 22px; bottom: 28px;
    font-family: "Noto Serif JP", serif; font-weight: 500; font-size: 26px;
  }
</style>
</head>
<body>
  <div class="pouch"></div>
  <main class="label">
    <header class="maker">
      <span class="maker-mark"></span>
      <span class="maker-name">HONAMI</span>
    </header>

    <div class="premium-band"><span class="premium-word">PREMIUM</span></div>

    <h1 class="product-name">玄米珈琲</h1>

    <p class="claim">自然栽培法で作った<br>農薬不使用の玄米を100%使用</p>

    <div class="badges">
      <div class="badge-row">
        <span class="badge">安心の素材</span>
        <span class="badge">身体に優しい</span>
      </div>
      <div class="badge-row">
        <span class="badge">ノンカフェイン</span>
        <span class="badge">ポリフェノール</span>
        <span class="badge">食物繊維</span>
      </div>
    </div>

    <div class="drip-photo" role="img" aria-label="ペーパーフィルターに湯を注いで玄米珈琲をドリップする写真と、周りに広がる玄米"></div>

    <span class="method-tag">ドリップ式</span>

    <span class="net-weight">200g</span>
  </main>
</body>
</html>
```